Tarnwick is a steel frame construction company that builds residential and commercial homes

1. Homepage (we are after a basic website)
Hero Section:
A full-width image or video showcasing steel frames in construction or a finished project.
Tagline: Short, impactful tagline (e.g., "Strong Structures for Tomorrow").
Call-to-Action (CTA): A prominent "Get a Quote" or "Contact Us" button.
About Us (Snapshot Section):

A few lines about the company, emphasizing experience, certifications, and commitment to quality.
Include a "Learn More" button linking to the detailed About Us page.
Products/Services Section:

Feature the main products like steel frames for industrial, residential, and commercial projects.
Each category should have a "Learn More" link to a dedicated product page.
Project Showcase/Portfolio:

Display 2-3 featured projects with images, descriptions, and a "View All Projects" button.
Certifications & Partners:

Display logos of certifications (QSB, local building standards) and partnerships with construction companies or industry bodies.
Footer:

Contact information, quick links (Home, About, Products, Services, Contact), and social media icons.
2. Products Page
Overview:

A grid or list layout showing different steel frame products or services.
Each product should have a title, brief description, and a thumbnail image.
Individual Product Pages:

Detailed information on specific products (e.g., “Steel Frames for Residential Construction”):
Features: Highlight specific features like durability, eco-friendliness, precision, etc.
Technical Specs: Material grades, dimensions, finishes available.
Case Studies: A couple of client testimonials or case studies of where this product was used.
Downloadable Resources:

Technical datasheets or catalogs for users to download.
Include a form to capture user information before they download the document (optional for lead generation).
3. Projects/Portfolio Page
Gallery of Projects:
Display completed projects with high-quality images, each linked to a project detail page.
Filter options (e.g., industrial, residential, commercial).
Project Detail Pages:
A detailed description of the project, challenges, and how the steel frames were used.
other website we liked are:
https://www.tarnwickbuilds.example/
https://orlenbayhomes.example/

1. Objective:
Create an informative, professional, and visually appealing website that promotes steel frame construction solutions, showcasing the company’s offerings, expertise, and projects.
The website should highlight the benefits of steel frames (e.g., durability, sustainability, and cost-efficiency) and cater to both B2B and B2C clients.
2. Target Audience:
Primary: Architects, builders, and construction companies.
Secondary: Homeowners, investors, and property developers looking for modern, durable construction solutions.

```html
<!DOCTYPE html>
<html lang="en">
<head>
<meta charset="utf-8">
<title>Tarnwick — Steel Frame Construction</title>
<link href="https://fonts.googleapis.com/css2?family=Archivo:wght@700;800;900&family=Arimo:wght@400;700&display=swap" rel="stylesheet">
<style>
:root{
  --blue:#0b6fc4;
  --navy:#16213e;
  --navy-deep:#142039;
  --ink:#14213d;
  --text:#5a6270;
  --sky:#e8f4fc;
  --sky-box:#e3f1fc;
  --line:#e6e9ee;
  --white:#fff;
  --orange:#f39a1f;
}
*{box-sizing:border-box;margin:0;padding:0}
html,body{width:1200px;height:4454px;overflow:hidden}
body{position:relative;font-family:"Arimo",Arial,sans-serif;color:var(--ink);background:var(--white)}
.abs{position:absolute}
.heading{font-family:"Archivo",Arial,sans-serif;font-weight:900;color:var(--ink);letter-spacing:-.2px}
.eyebrow{font-family:"Archivo",Arial,sans-serif;font-weight:800;font-size:12px;letter-spacing:2.4px;color:var(--blue);text-transform:uppercase}
.center{left:0;width:1200px;text-align:center}
.lead{font-size:13px;line-height:23px;color:var(--text)}
.btn{display:flex;align-items:center;justify-content:center;gap:7px;background:var(--blue);color:var(--white);font-family:"Archivo",Arial,sans-serif;font-weight:800;font-size:14px;border-radius:6px}
.btn svg{width:14px;height:14px}
.logo{display:flex;align-items:center;gap:10px;font-family:"Archivo",Arial,sans-serif;font-weight:900;color:var(--white);letter-spacing:1px}
.logo .mark{border:3px solid var(--white)}

/* hero */
.hero{left:31px;top:40px;width:1138px;height:707px;border-radius:34px;overflow:hidden;background:linear-gradient(180deg,#4a5661 0%,#3a3f44 45%,#4b4136 100%)}
.hero .shade{position:absolute;inset:0;background:rgba(10,14,20,.45)}
.nav a{position:absolute;top:27px;color:var(--white);font-size:13px;text-decoration:none}
.hero-title{font-size:54px;line-height:59px;color:var(--white)}
.hero-text{color:#eef1f4;font-size:15px;line-height:27px}
.btn-ghost{background:transparent;border:1.5px solid var(--white)}

/* about */
.photo{border-radius:22px}
.checks{left:602px;top:1094px;width:494px;height:139px;border-radius:14px;background:var(--sky-box);padding:25px 0 0 22px}
.checks li{list-style:none;display:flex;align-items:center;gap:9px;font-size:14px;color:#2a3142;height:35px}
.checks svg{width:15px;height:15px}

/* services */
.band{left:0;top:1400px;width:1200px;height:749px;background:var(--sky)}
.svc{top:1672px;width:266px;height:320px;border-radius:26px;overflow:hidden}
.svc .cap{position:absolute;left:31px;bottom:34px;color:var(--white);font-family:"Archivo",Arial,sans-serif;font-weight:800;font-size:17px;line-height:24px}

/* projects */
.proj{top:2421px;width:314px;height:401px;border:1px solid var(--line);border-radius:20px;overflow:hidden;background:var(--white)}
.proj .img{height:204px}
.proj h3{font-family:"Archivo",Arial,sans-serif;font-weight:700;font-size:18px;margin:26px 0 0 23px;color:var(--ink)}
.proj p{margin:14px 23px 0;font-size:13px;line-height:22px;color:var(--text)}
.proj .more{display:flex;align-items:center;gap:6px;margin:14px 0 0 23px;font-weight:700;font-size:13px;color:var(--blue)}
.proj .more svg{width:14px;height:14px}

/* cta */
.cta{left:0;top:2995px;width:1200px;height:406px;background:var(--navy)}

/* certs */
.badge{top:3674px;width:180px;height:175px;border:1px solid var(--line);border-radius:22px;display:flex;align-items:center;justify-content:center}
.dots{left:550px;top:3879px;display:flex;gap:10px}
.dots span{width:8px;height:8px;border-radius:50%;background:var(--blue)}
.dots span:first-child{background:var(--ink)}

/* footer */
.footer{left:0;top:3973px;width:1200px;height:481px;background:var(--navy-deep)}
.flink{display:flex;align-items:center;gap:9px;color:var(--white);font-size:13px}
.flink svg{width:16px;height:16px;flex:none}
.social{display:flex;gap:8px}
.social span{width:19px;height:19px;border-radius:50%;background:var(--blue)}
</style>
</head>
<body>

<svg width="0" height="0" style="position:absolute">
  <defs>
    <symbol id="arrow" viewBox="0 0 16 16"><circle cx="8" cy="8" r="7" fill="none" stroke="currentColor" stroke-width="1.4"/><path d="M5 8h6M8.5 5.5 11 8l-2.5 2.5" fill="none" stroke="currentColor" stroke-width="1.4" stroke-linecap="round" stroke-linejoin="round"/></symbol>
    <symbol id="tick" viewBox="0 0 16 16"><circle cx="8" cy="8" r="8" fill="#0b6fc4"/><path d="M4.5 8.2 7 10.5 11.5 5.8" fill="none" stroke="#fff" stroke-width="1.8" stroke-linecap="round" stroke-linejoin="round"/></symbol>
    <symbol id="phone" viewBox="0 0 24 24"><path d="M6.6 3.5 9 6.3c.5.6.4 1.4-.1 1.9L7.6 9.5c1.3 2.7 3.6 5 6.3 6.3l1.3-1.3c.5-.5 1.3-.6 1.9-.1l2.8 2.4c.6.5.6 1.4.1 2l-1.5 1.6c-.8.8-2 1.1-3.1.7C9.8 19.4 4.6 14.2 2.9 8.6c-.4-1.1-.1-2.300.7-3.1L5.2 4c.4-.6 1-.7 1.4-.5z" fill="none" stroke="currentColor" stroke-width="1.4" stroke-linejoin="round"/></symbol>
    <symbol id="pin" viewBox="0 0 24 24"><rect x="3" y="4" width="18" height="16" rx="2" fill="none" stroke="currentColor" stroke-width="1.4"/><path d="M15 9a2 2 0 1 1-4 0 2 2 0 0 1 4 0zM9 17c.6-2 2.2-3 4-3s3.4 1 4 3" fill="none" stroke="currentColor" stroke-width="1.4"/></symbol>
    <symbol id="mail" viewBox="0 0 24 24"><rect x="3" y="6" width="18" height="13" rx="2" fill="none" stroke="currentColor" stroke-width="1.4"/><path d="m3.5 7 8.5 6.5L20.5 7" fill="none" stroke="currentColor" stroke-width="1.4"/></symbol>
  </defs>
</svg>

<!-- Hero -->
<section class="hero abs" role="img" aria-label="Steel frame building under construction with exposed columns and roof trusses">
  <div class="shade"></div>
  <div class="logo abs" style="left:76px;top:33px;font-size:24px"><span class="mark" style="width:18px;height:18px"></span>TARNWICK</div>
  <nav class="nav">
    <a style="left:413px">Home</a><a style="left:482px">About Us</a><a style="left:571px">Products</a><a style="left:657px">Services</a><a style="left:744px">Projects</a>
  </nav>
  <div class="btn abs" style="left:930px;top:12px;width:132px;height:47px;font-size:13px">Contact Us</div>
  <div class="eyebrow abs" style="left:0;width:1138px;text-align:center;top:236px;font-size:11px">Welcome to Tarnwick</div>
  <h1 class="heading hero-title abs" style="left:0;width:1138px;text-align:center;top:267px">Strong Structures for<br>Tomorrow</h1>
  <p class="hero-text abs" style="left:0;width:1138px;text-align:center;top:408px">we specialize in turning visions into reality with exceptional craftsmanship and meticulous<br>attention to detail. With years of experience and a commitment to quality.</p>
  <div class="btn abs" style="left:386px;top:496px;width:159px;height:47px;font-size:14px">Get Started <svg><use href="#arrow"/></svg></div>
  <div class="btn btn-ghost abs" style="left:572px;top:496px;width:179px;height:47px;font-size:14px">View Projects <svg><use href="#arrow"/></svg></div>
</section>

<!-- About -->
<div class="photo abs" style="left:104px;top:951px;width:399px;height:347px;background:linear-gradient(160deg,#c9a57a 0%,#e27a2a 55%,#7b5f4a 100%)" role="img" aria-label="Two construction workers in hard hats and safety vests"></div>
<div class="eyebrow abs" style="left:602px;top:825px">About us</div>
<h2 class="heading abs" style="left:602px;top:855px;font-size:44px;line-height:48px">Crafting structures<br>that last a lifetime</h2>
<p class="lead abs" style="left:602px;top:972px;width:475px">Crafting structures that last a lifetime requires a holistic approach that integrates advanced materials, resilient design, regular maintenance, and sustainability practices. By learning from historical examples and leveraging modern technology.</p>
<ul class="checks abs">
  <li><svg><use href="#tick"/></svg>Comprehensive Services</li>
  <li><svg><use href="#tick"/></svg>Advanced Technology</li>
  <li><svg><use href="#tick"/></svg>Transparent Communication</li>
</ul>
<div class="btn abs" style="left:602px;top:1273px;width:186px;height:48px">Get Free Quote <svg><use href="#arrow"/></svg></div>
<svg class="abs" style="left:810px;top:1280px;width:34px;height:34px;color:var(--orange)"><use href="#phone"/></svg>
<div class="abs" style="left:859px;top:1277px;font-size:11px;color:var(--text)">call support center 24X7</div>
<div class="abs" style="left:859px;top:1298px;font-family:Archivo,Arial,sans-serif;font-weight:800;font-size:19px">+1 555 014 2290</div>

<!-- Services -->
<section class="band abs"></section>
<div class="eyebrow abs center" style="top:1480px">Our services</div>
<h2 class="heading abs center" style="top:1508px;font-size:44px">Products &amp; Services</h2>
<p class="lead abs center" style="top:1578px">We specialize in a wide range of construction services, including residential, commercial, and industrial<br>projects.</p>
<div class="svc abs" style="left:31px;background:linear-gradient(180deg,#a9c3dc 0%,#5b6877 55%,#12161c 100%)" role="img" aria-label="Modular steel frame structure against a blue sky"><div class="cap">Modular Steel Frame</div></div>
<div class="svc abs" style="left:322px;background:linear-gradient(180deg,#7b7d80 0%,#9a5a3a 55%,#15181c 100%)" role="img" aria-label="Multi-storey building clad with dry construction panels"><div class="cap">Dry Construction<br>System</div></div>
<div class="svc abs" style="left:612px;background:linear-gradient(180deg,#cfd6dc 0%,#6f7780 55%,#14181c 100%)" role="img" aria-label="Warehouse steel frame skeleton with crane"><div class="cap">Warehouse Steel<br>Frame</div></div>
<div class="svc abs" style="left:903px;background:linear-gradient(180deg,#c7d7e6 0%,#55585b 55%,#121518 100%)" role="img" aria-label="Modern luxury villa with dark facade"><div class="cap">Homes &amp; Luxury Villas</div></div>
<div class="btn abs" style="left:496px;top:2040px;width:206px;height:47px">View All Services <svg><use href="#arrow"/></svg></div>

<!-- Projects -->
<div class="eyebrow abs center" style="top:2229px">Our projects</div>
<h2 class="heading abs center" style="top:2257px;font-size:44px">Explore our diverse range of projects</h2>
<p class="lead abs center" style="top:2328px">We specialize in a wide range of construction services, including residential, commercial, and industrial<br>projects.</p>
<article class="proj abs" style="left:104px"><div class="img" style="background:linear-gradient(180deg,#9aa3ab,#6a5444)" role="img" aria-label="Concrete high-rise under construction with tower crane"></div><h3>Project # 01</h3><p>Our post-construction services gives you peace of mind knowing that we are still here for you even after.</p><div class="more">Read More <svg style="color:var(--orange)"><use href="#arrow"/></svg></div></article>
<article class="proj abs" style="left:443px"><div class="img" style="background:linear-gradient(180deg,#8c9aa8,#6f6f6c)" role="img" aria-label="Building site with formwork and scaffolding"></div><h3>Project # 02</h3><p>Our post-construction services gives you peace of mind knowing that we are still here for you even after.</p><div class="more">Read More <svg style="color:var(--orange)"><use href="#arrow"/></svg></div></article>
<article class="proj abs" style="left:781px"><div class="img" style="background:linear-gradient(180deg,#a2835f,#4b4a47)" role="img" aria-label="Aerial view of a concrete frame construction site"></div><h3>Project # 03</h3><p>Our post-construction services gives you peace of mind knowing that we are still here for you even after.</p><div class="more">Read More <svg style="color:var(--orange)"><use href="#arrow"/></svg></div></article>
<div class="btn abs" style="left:498px;top:2884px;width:202px;height:47px">View All Projects <svg><use href="#arrow"/></svg></div>

<!-- CTA -->
<section class="cta abs"></section>
<h2 class="heading abs" style="left:104px;top:3072px;font-size:44px;line-height:49px;color:var(--white)">Let's bulid something<br>great together!</h2>
<p class="abs" style="left:104px;top:3191px;font-size:13px;line-height:23px;color:#e4e8ef">Don't wait any longer to bring your construction dreams to life. Partner with Tarnwick and<br>experience unparalleled service and quality.</p>
<div class="btn abs" style="left:104px;top:3268px;width:206px;height:53px">Get Free Quote <svg><use href="#arrow"/></svg></div>
<div class="abs" style="left:700px;top:3047px;width:363px;height:354px;background:linear-gradient(180deg,#f39a1f 0%,#e0602a 55%,#d94a22 100%);border-radius:160px 160px 0 0;opacity:.9" role="img" aria-label="Construction worker in hard hat and orange vest pointing left"></div>

<!-- Certifications -->
<div class="eyebrow abs center" style="top:3479px">Our affiliates</div>
<h2 class="heading abs center" style="top:3507px;font-size:44px">Certifications &amp; Partners</h2>
<p class="lead abs center" style="top:3580px">We specialize in a wide range of construction services, including residential, commercial, and industrial<br>projects.</p>
<div class="badge abs" style="left:104px" role="img" aria-label="Partner badge"><svg width="96" height="116"><rect x="4" y="4" width="88" height="108" rx="10" fill="#b01f2a"/></svg></div>
<div class="badge abs" style="left:306px" role="img" aria-label="Quality certification badge"><svg width="130" height="110"><circle cx="65" cy="55" r="52" fill="#1d55a6"/></svg></div>
<div class="badge abs" style="left:510px" role="img" aria-label="Conformity badge"><svg width="110" height="90"><rect x="5" y="5" width="100" height="80" rx="8" fill="#111"/></svg></div>
<div class="badge abs" style="left:712px" role="img" aria-label="Certification badge"><svg width="124" height="124"><circle cx="62" cy="62" r="58" fill="#f08a24"/></svg></div>
<div class="badge abs" style="left:916px" role="img" aria-label="Industry body badge"><svg width="104" height="104"><circle cx="52" cy="52" r="50" fill="#222"/></svg></div>
<div class="dots abs"><span></span><span></span><span></span><span></span><span></span><span></span></div>

<!-- Footer -->
<footer class="footer abs"></footer>
<div class="logo abs" style="left:0;width:1200px;justify-content:center;top:4082px;font-size:28px"><span class="mark" style="width:22px;height:22px"></span>TARNWICK</div>
<div class="flink abs" style="left:104px;top:4185px"><svg style="color:var(--orange)"><use href="#arrow"/></svg>About Us</div>
<div class="flink abs" style="left:104px;top:4224px"><svg style="color:var(--orange)"><use href="#arrow"/></svg>Products &amp; Services</div>
<div class="flink abs" style="left:358px;top:4185px"><svg style="color:var(--orange)"><use href="#arrow"/></svg>Our Projects</div>
<div class="flink abs" style="left:358px;top:4224px"><svg style="color:var(--orange)"><use href="#arrow"/></svg>Contact Us</div>
<div class="flink abs" style="left:612px;top:4185px"><svg style="color:var(--orange)"><use href="#phone"/></svg>+1 555 014 2290</div>
<div class="flink abs" style="left:612px;top:4234px"><svg style="color:var(--orange)"><use href="#mail"/></svg>info@tarnwick.example</div>
<div class="flink abs" style="left:864px;top:4185px;align-items:flex-start;line-height:22px"><svg style="color:var(--orange);margin-top:2px"><use href="#pin"/></svg>48 Ferrow Lane Dockside<br>Court 11B,4102 QL</div>
<div class="social abs" style="left:897px;top:4241px"><span></span><span></span><span></span><span></span><span></span></div>
<div class="abs" style="left:104px;top:4305px;width:992px;height:1px;background:rgba(255,255,255,.12)"></div>
<div class="abs center" style="top:4343px;font-size:12px;color:var(--white)">Copyright © 2024 Tarnwick. All Rights Reserved.</div>

</body>
</html>
```